Avocado Smoothies (100% Natural, No Preservatives, No added Sugar)

We need a company logo (for business cards etc) as well as label design (front and back) for a range of avocado based smoothies on our 300 ml bottle & pouch with drinking spout. The look & feel of the label is that the smoothies are fresh & healthy, prepared with freshest ingredients & formulated with nutritional needs in mind.

The final design should give the impression of a genuine & trusted brand of beverage that is appealing to (1) health conscious busy professionals both male & female (e.g. gym / yoga / athletic buffs), (2) busy mothers of fussy / picky kids; and (3) people who like more plant-based diets, who want the best products for them / their families. The design is to be innovative & appealing to the intelligent health conscious consumers especially avocado fans, looking for healthier alternatives of natural drinks on-the go, that are NOT prepared by big, impersonal & highly automated factories that use all sorts of nasties & processes in their beverages. Easy to read FONT and preferably include an original picture of avocado (which can be a real picture / graphic design) - however, this is not necessary.

Company name: OMBRA Pte.Ltd. (the letter "I" may mean "I" or "Innovative" or "Intelligent". "OMBRA" can be a play of the word "I ever .... " e.g. "all OMBRA wanted is ... ".)

Please note that the master label design should be versatile enough for a range of avocado smoothies (we only need to make minimum changes to the main picture / words as necessary for each specific avocado smoothie) and the label can also be used for kids size and adult size pouches and bottles of height 16cm and diameter of circular base of 5.5cm.

Target Market(s)

(1) health conscious busy professionals (e.g. gym / yoga / athletic buffs), (2) busy mothers of fussy / picky kids; and (3) vegans & people who like more plant based diets, who want the best products for them / their families.

Logo Text

OMBRA

Font styles to use
Serif
Sans Serif
Decorative
Script

Colors

Designer to choose colors to be used in the design.

Requirements
Must have
• Centre attention of the label (BIG font): Avocado & [we insert the other main ingredients] Smoothie
• Company logo (noticeable somewhere on the label): OMBRA
• (Medium font) All natural ingredients, no added sugar or salt, no additives or preservatives
• (Smaller fonts) Along the lines of: "Made from the finest blend of avocados and [we can insert other ingredients] to nourish you. Rich, creamy, wholesome & unique avocado experience that is good and satisfyingly delicious! "
• Keep refrigerated below 5 deg C
• Manufactured by: [we insert details]
• 300ml
Nice to have
• Please recycle usual logo
• originality & fresh & appealing factor
Should not have
• unhealthy image / junk food / sugary / additives / unsavoury impression
• difficult to read font
• confusion with other existing brands

```html
<!DOCTYPE html>
<html lang="en">
<head>
<meta charset="utf-8">
<title>OMBRA Avocado Orange Smoothie Label</title>
<link href="https://fonts.googleapis.com/css2?family=Poppins:wght@400;700;800&display=swap" rel="stylesheet">
<style>
  :root {
    --backdrop: #d9ebe5;
    --mint: #a9d9c4;
    --peach: #f6cf8a;
    --teal: #1f9a8e;
    --white: #ffffff;
    --orange-text: #ef7a1c;
    --volume: #e0521a;
    --fruit-green: #6b8e3a;
    --fruit-dark: #3f5e26;
    --fruit-orange: #f29a2e;
  }
  html, body {
    margin: 0;
    padding: 0;
    width: 1200px;
    height: 900px;
    overflow: hidden;
    background: var(--backdrop);
    font-family: "Poppins", sans-serif;
  }
  .label {
    position: absolute;
    left: 400px;
    top: 40px;
    width: 400px;
    height: 820px;
    background: var(--mint);
    overflow: hidden;
  }
  .label__lower {
    position: absolute;
    left: 0;
    top: 0;
    width: 400px;
    height: 820px;
  }
  .brand {
    position: absolute;
    left: 22px;
    top: 60px;
    transform-origin: left top;
    transform: rotate(90deg) translate(0, -28px);
    font-weight: 700;
    font-size: 28px;
    letter-spacing: 2px;
    color: var(--teal);
    line-height: 1;
    margin: 0;
  }
  .hero-fruit {
    position: absolute;
    left: 98px;
    top: 150px;
    width: 196px;
    height: 420px;
    border-radius: 48% 48% 50% 50% / 38% 38% 30% 30%;
    background: linear-gradient(to bottom, var(--fruit-green) 0%, var(--fruit-dark) 55%, var(--fruit-orange) 70%, var(--fruit-orange) 100%);
  }
  .title {
    position: absolute;
    left: 0;
    top: 360px;
    width: 400px;
    margin: 0;
    text-align: center;
    color: var(--white);
    font-weight: 800;
    font-size: 66px;
    line-height: 86px;
    letter-spacing: -1px;
  }
  .title span { display: block; }
  .description {
    position: absolute;
    left: 26px;
    top: 628px;
    width: 300px;
    margin: 0;
    font-size: 12.5px;
    line-height: 18px;
    color: var(--orange-text);
  }
  .storage {
    position: absolute;
    left: 26px;
    top: 738px;
    margin: 0;
    font-size: 13px;
    font-weight: 700;
    color: var(--white);
  }
  .volume {
    position: absolute;
    right: 26px;
    top: 730px;
    margin: 0;
    font-size: 21px;
    font-weight: 700;
    color: var(--volume);
  }
</style>
</head>
<body>
  <main class="label">
    <svg class="label__lower" viewBox="0 0 400 820" aria-hidden="true">
      <path d="M0 450 Q 25 438 50 450 T 100 450 T 150 450 T 200 450 T 250 450 T 300 450 T 350 450 T 400 450 V 820 H 0 Z" fill="var(--peach)"/>
    </svg>
    <div class="hero-fruit" role="img" aria-label="Photo of a whole avocado with a leaf on its stem, its lower half shown as an orange"></div>
    <p class="brand">OMBRA</p>
    <h1 class="title"><span>AVOCADO</span><span>ORANGE</span></h1>
    <p class="description">Made from the finest blend of avocados and oranges to nourish you. Rich, creamy, wholesome &amp; unique avocado experience that is good and satisfyingly delicious!</p>
    <p class="storage">Keep refrigerated below 5ºC</p>
    <p class="volume">300ml</p>
  </main>
</body>
</html>
```